Healthy Meal Delivery Website Needs to be updated, current, fresh and modern

Hi there,

The current website i have is super old and outdated.

I would like a beautiful modern site that has all the same content as the previous except with a a new, modern and trustworthy feel.

The current website is https://velmorplatekitchen.com/

Target Market(s)

Health Conscious Young Professionals

Industry/Entity Type

Food Service

Font styles to use
Sans Serif

Requirements
Must have
• Modern Trustworthy feel
Should not have
• Anything out dated or cheesy or scammy

```html
<!DOCTYPE html>
<html lang="en">
<head>
<meta charset="utf-8">
<title>Velmor Plate Kitchen – Fresh Diet Meals Delivered</title>
<link href="https://fonts.googleapis.com/css2?family=Rajdhani:wght@600;700&family=Oxygen:wght@400;700&display=swap" rel="stylesheet">
<style>
:root{
  --blue:#1c9fe0;
  --blue-dark:#1587c2;
  --yellow:#f2e31c;
  --ink:#1f2428;
  --text:#3d4348;
  --muted:#6b7278;
  --white:#ffffff;
  --pale:#dbeef8;
  --green:#4f8a2c;
}
*{margin:0;padding:0;box-sizing:border-box}
html,body{width:1200px;height:3991px;overflow:hidden}
body{font-family:"Oxygen",Arial,sans-serif;color:var(--text);background:var(--white);position:relative}
.head{font-family:"Rajdhani","Arial Narrow",sans-serif;font-weight:700;text-transform:uppercase;letter-spacing:.5px}
.abs{position:absolute}
a{color:inherit;text-decoration:none}

/* top bar */
.topbar{position:absolute;left:0;top:0;width:1200px;height:32px;background:rgba(255,255,255,.92);z-index:3;font-size:12px;color:var(--text)}
.topbar .contact{position:absolute;left:100px;top:9px;display:flex;gap:26px}
.topbar .contact span{display:flex;align-items:center;gap:6px}
.social{display:flex;gap:4px}
.social i{display:block;width:24px;height:24px;background:var(--blue)}
.topbar .social{position:absolute;right:34px;top:4px}

/* nav */
.nav{position:absolute;left:0;top:32px;width:1200px;height:80px;background:rgba(255,255,255,.88);z-index:3}
.brand{display:flex;align-items:center;gap:12px;font-family:"Rajdhani",sans-serif;font-weight:700;font-size:22px;color:var(--blue)}
.brand .mark{width:44px;height:44px;background:var(--yellow)}
.nav .brand{position:absolute;left:82px;top:18px}
.menu{position:absolute;left:415px;top:32px;display:flex;gap:34px;font-size:12px;font-weight:700;color:var(--ink);letter-spacing:.3px}
.menu .on{color:var(--blue);border-bottom:2px solid var(--blue);padding-bottom:4px}
.btn{display:inline-block;background:var(--blue);color:var(--white);font-size:12px;font-weight:700;text-transform:uppercase;padding:12px 22px;letter-spacing:.4px}
.nav .btn.signup{position:absolute;left:938px;top:22px}
.nav .btn.login{position:absolute;left:1036px;top:22px;padding:12px 26px}

/* hero */
.hero{position:absolute;left:0;top:0;width:1200px;height:600px;background:linear-gradient(100deg,#3f4a2e 0%,#5d6a3d 35%,#c9b94a 62%,#e7d646 78%,#dfe6de 100%);overflow:hidden}
.hero .shade{position:absolute;inset:0;background:linear-gradient(90deg,rgba(0,0,0,.45),rgba(0,0,0,.05) 60%)}
.hero h1{position:absolute;left:155px;top:258px;color:var(--white);font-size:50px;line-height:1}
.hero ul{position:absolute;left:152px;top:336px;list-style:none;color:var(--white);font-size:19px;line-height:27px}
.hero li::before{content:"»";margin-right:10px}
.arrow{position:absolute;width:40px;height:40px;border-radius:50%;display:flex;align-items:center;justify-content:center}
.hero .prev{left:0;top:340px;background:rgba(255,255,255,.45);border-radius:0 50% 50% 0}
.hero .next{left:1142px;top:340px;background:var(--blue)}

/* what is */
.what h2{position:absolute;left:155px;top:700px;font-size:38px;color:var(--blue)}
.what h2 b{color:var(--ink)}
.what .rule{position:absolute;left:155px;top:746px;width:70px;height:3px;background:var(--blue)}
.what p{position:absolute;left:155px;width:560px;font-size:14.5px;line-height:23px}
.what .photo{position:absolute;left:740px;top:687px;width:228px;height:358px;background:linear-gradient(180deg,#1f3b16,#3f7b25 40%,#6ea83c 70%,#2a4a1c);box-shadow:0 10px 24px rgba(0,0,0,.35)}
.circle{position:absolute;border-radius:50%;background:var(--pale)}

/* blue band */
.band{position:absolute;left:0;top:1131px;width:1200px;height:567px;background:var(--blue);color:var(--white)}
.band h2{position:absolute;left:0;width:1200px;top:58px;text-align:center;font-size:36px;line-height:40px}
.band h2 em{font-style:normal;color:var(--ink)}
.band .lead{position:absolute;left:220px;width:760px;top:170px;text-align:center;font-size:14px;line-height:23px}
.feature{position:absolute;top:262px;width:210px;text-align:center}
.feature svg{display:block;margin:0 auto}
.feature h3{font-size:20px;margin-top:14px}
.feature p{font-size:12.5px;line-height:19px;margin-top:10px}
.feature .more{display:inline-block;margin-top:14px;font-size:11px;font-weight:700;text-decoration:underline;color:var(--ink)}
.feature.card{background:var(--white);color:var(--text);box-shadow:0 8px 20px rgba(0,0,0,.2);padding:22px 18px 26px;top:255px;height:264px}
.feature.card h3{color:var(--blue)}

/* menu */
.menu-sec h2{position:absolute;left:0;width:1200px;top:1765px;text-align:center;font-size:38px;color:var(--blue)}
.menu-sec h2 b{color:var(--ink)}
.menu-sec .lead{position:absolute;left:0;width:1200px;top:1828px;text-align:center;font-size:14.5px;line-height:23px}
.dish{position:absolute;top:1908px;width:282px}
.dish .pic{height:168px}
.dish .tag{height:26px;background:var(--blue);color:var(--white);font-size:12px;font-weight:700;padding:6px 12px;text-transform:uppercase;display:flex;align-items:center;gap:8px}
.dish .tag i{width:9px;height:9px;background:var(--white);transform:rotate(45deg)}
.dish.active .tag{background:var(--yellow);color:var(--ink)}
.dish.active .tag i{background:var(--ink)}
.dish h4{font-size:15px;font-weight:700;color:var(--ink);margin-top:14px;line-height:20px}
.dish.active h4{color:var(--blue);text-decoration:underline}
.dots{position:absolute;display:flex;gap:6px}
.dots i{width:16px;height:6px;border-radius:3px;background:#a8b3ba}
.dots i.on{background:var(--blue)}

/* plan */
.plan{position:absolute;left:0;top:2262px;width:1200px;height:559px;background:linear-gradient(110deg,#2c2a18 0%,#5b4a22 30%,#8d6a30 55%,#4a5a26 80%,#2f3a1c 100%);overflow:hidden;color:var(--white)}
.plan .shade{position:absolute;inset:0;background:linear-gradient(90deg,rgba(0,0,0,.55),rgba(0,0,0,.15))}
.plan h2{position:absolute;left:155px;top:98px;font-size:40px}
.plan h2 em{font-style:normal;color:var(--blue)}
.plan .sub{position:absolute;left:155px;top:142px;font-size:13px}
.plan h5{position:absolute;left:155px;font-size:17px;font-weight:700}
.plan p{position:absolute;left:155px;width:360px;font-size:13px;line-height:20px}
.plan .bowl{position:absolute;left:723px;top:26px;width:400px;height:400px;border-radius:50%;background:radial-gradient(circle at 45% 45%,#7a2030 0%,#3c3f6c 30%,#3f7a2a 60%,#e5e6e0 82%)}

/* testimonial */
.say h2{position:absolute;left:0;width:1200px;top:2875px;text-align:center;font-size:38px;color:var(--blue)}
.say h2 b{color:var(--ink)}
.say .q{position:absolute;left:0;width:1200px;top:2960px;text-align:center;font-family:Georgia,serif;font-size:60px;font-weight:700;color:var(--blue);line-height:60px}
.say blockquote{position:absolute;left:275px;width:650px;top:3030px;text-align:center;font-size:14px;line-height:23px}
.say .avatar{position:absolute;left:566px;top:3148px;width:70px;height:70px;border-radius:50%;background:linear-gradient(135deg,#c6a68c,#6b5243)}
.say .name{position:absolute;left:0;width:1200px;top:3242px;text-align:center;font-size:16px;color:var(--blue)}

/* cta */
.cta{position:absolute;left:0;top:3326px;width:1200px;height:338px;background:linear-gradient(100deg,#7a3a12 0%,#b5542a 25%,#4f6a26 55%,#3c5a1e 75%,#6a4f2a 100%);color:var(--white);overflow:hidden}
.cta .shade{position:absolute;inset:0;background:rgba(0,0,0,.48)}
.cta h2{position:absolute;left:0;width:1200px;top:92px;text-align:center;font-size:38px;line-height:40px}
.cta h2 em{font-style:normal;color:var(--blue)}
.cta p{position:absolute;left:300px;width:600px;top:178px;text-align:center;font-size:14px;line-height:22px}
.cta .btn{position:absolute;top:240px}
.cta .btn.ghost{background:var(--white);color:var(--blue);left:450px;padding:12px 26px}
.cta .btn.solid{left:612px;padding:12px 32px}

/* footer */
.foot .brand{position:absolute;left:468px;top:3728px;font-size:24px}
.foot .links{position:absolute;left:0;width:1200px;top:3797px;display:flex;justify-content:center;gap:14px;font-size:12px;font-weight:700;color:var(--ink)}
.foot .links .on{color:var(--blue)}
.foot h3{position:absolute;left:0;width:1200px;top:3840px;text-align:center;font-size:30px;color:var(--blue)}
.foot h3 b{color:var(--ink)}
.foot .contact{position:absolute;left:0;width:1200px;top:3880px;text-align:center;font-size:13px}
.foot .contact b{color:var(--blue)}
.foot .up{position:absolute;left:1142px;top:3890px}
.bottombar{position:absolute;left:0;top:3965px;width:1200px;height:26px;background:var(--blue);color:var(--white);font-size:11px}
.bottombar span{position:absolute;left:176px;top:6px}
.bottombar .social{position:absolute;right:150px;top:2px}
.bottombar .social i{background:var(--white);opacity:.85;width:22px;height:22px}
</style>
</head>
<body>

<div class="topbar">
  <div class="contact">
    <span><svg width="11" height="11" viewBox="0 0 24 24"><path d="M6.6 10.8a15 15 0 0 0 6.6 6.6l2.2-2.2c.3-.3.7-.4 1-.2 1.1.4 2.3.6 3.6.6.6 0 1 .4 1 1V20c0 .6-.4 1-1 1A17 17 0 0 1 3 4c0-.6.4-1 1-1h3.5c.6 0 1 .4 1 1 0 1.3.2 2.5.6 3.6.1.3 0 .7-.2 1z" fill="#1c9fe0"/></svg>(416) 555-0188</span>
    <span><svg width="12" height="10" viewBox="0 0 24 18"><rect x="1" y="1" width="22" height="16" fill="none" stroke="#1c9fe0" stroke-width="2"/><path d="M1 1l11 9 11-9" fill="none" stroke="#1c9fe0" stroke-width="2"/></svg>sales@velmorplatekitchen.com</span>
  </div>
  <div class="social"><i></i><i></i><i></i><i></i><i></i></div>
</div>

<header class="nav">
  <div class="brand"><span class="mark"></span>Velmor Plate Kitchen</div>
  <nav class="menu">
    <a class="on">HOME</a><a>VELMOR MEAL PLANS</a><a>MENU</a><a>PRICING</a><a>ABOUT</a><a>PRESS</a><a>CONTACT</a>
  </nav>
  <a class="btn signup">Sign Up</a>
  <a class="btn login">Login</a>
</header>

<section class="hero" role="img" aria-label="Smiling woman in a yellow top drinking a green smoothie in a bright kitchen with vegetables">
  <div class="shade"></div>
  <h1 class="head">Fresh Diet Meals Delivered</h1>
  <ul>
    <li>Real food you'll love to eat</li>
    <li>Portion controlled meals to maximize your weight loss</li>
    <li>No grocery shopping, cooking or cleaning required</li>
    <li>Freshly prepared by our in house chefs</li>
  </ul>
  <div class="arrow prev"><svg width="14" height="14" viewBox="0 0 24 24"><path d="M15 4l-8 8 8 8" fill="none" stroke="#fff" stroke-width="3"/></svg></div>
  <div class="arrow next"><svg width="14" height="14" viewBox="0 0 24 24"><path d="M9 4l8 8-8 8" fill="none" stroke="#fff" stroke-width="3"/></svg></div>
</section>

<section class="what">
  <div class="circle" style="left:-70px;top:560px;width:180px;height:180px;opacity:.6"></div>
  <div class="circle" style="left:980px;top:560px;width:200px;height:200px;opacity:.7"></div>
  <h2 class="head">What is <b>Velmor?</b></h2>
  <div class="rule"></div>
  <p style="top:775px">Velmor is the Toronto &amp; Montreal Diet Delivery program based on the Velmor Plan™, healthy carbs and the right fats.</p>
  <p style="top:830px">We provide you with 3 fresh meals, 2 snacks and a dessert delivered to your door before 6am.</p>
  <p style="top:885px">Try our Velmor Plan™ delivery plan and start Velmor weight loss now!</p>
  <a class="btn abs" style="left:155px;top:945px;padding:11px 28px">Explore More</a>
  <div class="photo" role="img" aria-label="Tall glass of green smoothie with a straw beside green apples and leafy greens"></div>
</section>

<section class="band">
  <h2 class="head">The Velmor Plan <em>delivers diet meals</em> to your door<br>in Toronto, GTA and Montreal</h2>
  <p class="lead">Our fresh and delicious diet meals and snacks are made with only the best natural ingredients that nourish your body. Why not let us prepare your meals while you lose the weight?</p>

  <div class="feature" style="left:95px">
    <svg width="58" height="54" viewBox="0 0 58 54" fill="none" stroke="#fff" stroke-width="2.5"><path d="M6 26h46c0 13-10 22-23 22S6 39 6 26z"/><path d="M18 20c0-6 6-6 6-12M30 20c0-6 6-6 6-12"/><path d="M20 48h18"/></svg>
    <h3 class="head">Healthy</h3>
    <p>The Velmor Plan is a great way to ensure you are eating all the nutrients you need...</p>
    <a class="more">READ MORE</a>
  </div>
  <div class="feature" style="left:360px">
    <svg width="58" height="54" viewBox="0 0 58 54" fill="none" stroke="#fff" stroke-width="2.5"><rect x="10" y="8" width="38" height="38"/><path d="M18 26l9 9 22-26"/></svg>
    <h3 class="head">Choice</h3>
    <p>You can choose your own meals from over 100 tasty entrees, desserts and snack foods...</p>
    <a class="more">READ MORE</a>
  </div>
  <div class="feature card" style="left:631px;width:203px">
    <svg width="58" height="54" viewBox="0 0 58 54" fill="none" stroke="#1c9fe0" stroke-width="2.5"><path d="M12 22a18 18 0 0 1 32-6"/><path d="M44 8v8h-8"/><path d="M46 32a18 18 0 0 1-32 6"/><path d="M14 46v-8h8"/></svg>
    <h3 class="head">Fresh</h3>
    <p>All of our meals are real food, freshly prepared by our in-house expert chefs.</p>
    <a class="more" style="color:var(--blue)">READ MORE</a>
  </div>
  <div class="feature" style="left:895px">
    <svg width="58" height="54" viewBox="0 0 58 54" fill="none" stroke="#fff" stroke-width="2.5"><circle cx="29" cy="27" r="20"/><path d="M20 27l6 6 12-13"/></svg>
    <h3 class="head">Customized</h3>
    <p>Your meals will be delivered fresh to your door, customized for your unique body type...</p>
    <a class="more">READ MORE</a>
  </div>
</section>

<section class="menu-sec">
  <h2 class="head">Select from<b>over</b> 100 menu items</h2>
  <p class="lead">You can choose your own meals from over 100 tasty entrees, desserts and snack foods.<br>You can choose your meals online, or we can select your meals for you.</p>

  <div class="arrow" style="left:76px;top:2009px;width:34px;height:34px;background:var(--ink)"><svg width="12" height="12" viewBox="0 0 24 24"><path d="M15 4l-8 8 8 8" fill="none" stroke="#fff" stroke-width="3"/></svg></div>
  <div class="arrow" style="left:1088px;top:2009px;width:34px;height:34px;background:var(--blue)"><svg width="12" height="12" viewBox="0 0 24 24"><path d="M9 4l8 8-8 8" fill="none" stroke="#fff" stroke-width="3"/></svg></div>

  <div class="dish" style="left:154px">
    <div class="pic" role="img" aria-label="Grilled chicken strips over a green salad" style="background:linear-gradient(160deg,#c98a3c,#e3b86a 45%,#6d9a3a)"></div>
    <div class="tag"><i></i>Lunch</div>
    <h4>Grilled Chicken Salad</h4>
  </div>
  <div class="dish active" style="left:460px">
    <div class="pic" role="img" aria-label="Flat iron steak with roasted vegetables" style="background:linear-gradient(160deg,#4a2a18,#7a4524 45%,#b9772f 75%,#6b8a3a)"></div>
    <div class="tag"><i></i>Dinner</div>
    <h4>Flat Iron Steak With Roasted<br>Vegetables</h4>
  </div>
  <div class="dish" style="left:765px">
    <div class="pic" role="img" aria-label="Lettuce wraps filled with chicken and vegetables" style="background:linear-gradient(160deg,#dfe3d4,#a9c27a 45%,#e7ead8)"></div>
    <div class="tag"><i></i>Afternoon Snack</div>
    <h4>Cobb Lettuce Wrap</h4>
  </div>
  <div class="dots" style="left:570px;top:2190px"><i></i><i class="on"></i><i></i></div>
</section>

<section class="plan">
  <div class="abs" role="img" aria-label="Blurred background of fresh salad vegetables" style="inset:0"></div>
  <div class="shade"></div>
  <div class="circle" style="left:700px;top:-60px;width:118px;height:118px;opacity:.85"></div>
  <div class="circle" style="left:798px;top:430px;width:170px;height:170px;opacity:.85"></div>
  <div class="bowl" role="img" aria-label="Bowl of mixed berries and strawberries on greens"></div>
  <h2 class="head">The Velmor <em>Plan</em></h2>
  <div class="sub">Real foods designed by nature prepared by Velmor</div>
  <h5 style="top:190px">What You Get</h5>
  <p style="top:220px">Velmor Diet Delivery provides you with 3 fresh daily meals and 3 snacks delivered to your doorstep before 6am.</p>
  <h5 style="top:290px">Selection</h5>
  <p style="top:320px">Choose your meals from over 100 delicious entrees, snacks and desserts.</p>
  <div class="dots" style="left:155px;top:452px"><i></i><i class="on"></i><i></i></div>
</section>

<section class="say">
  <h2 class="head">What <b>they say</b></h2>
  <div class="q">“</div>
  <blockquote>" I would like to take this opportunity to thank you for your wonderful service and the months of delicious and nutritious meals that I have received. Now I embark on a new leg of my journey where I try to go it alone. I know that I am better prepared with the help that you provided.<br>* Thanks again and all the best"</blockquote>
  <svg class="abs" style="left:458px;top:3174px" width="14" height="14" viewBox="0 0 24 24"><path d="M15 4l-8 8 8 8" fill="none" stroke="#1f2428" stroke-width="3"/></svg>
  <div class="avatar" role="img" aria-label="Customer portrait"></div>
  <div class="arrow" style="left:718px;top:3164px;width:34px;height:34px;background:var(--blue)"><svg width="12" height="12" viewBox="0 0 24 24"><path d="M9 4l8 8-8 8" fill="none" stroke="#fff" stroke-width="3"/></svg></div>
  <div class="name head">Marla</div>
</section>

<section class="cta">
  <div class="abs" role="img" aria-label="Table of fresh vegetables, tomatoes, bread and whole foods" style="inset:0"></div>
  <div class="shade"></div>
  <h2 class="head">The Velmor Plan is based on real foods made with<br><em>fresh and natural ingredients.</em></h2>
  <p>It's about eating the foods you love and emphasizing the ones that nourish your body: generous portions of fresh fruit, vegetables, meat, fish, nuts and seeds, with smaller servings of grains and dairy.</p>
  <a class="btn ghost">Customer Login</a>
  <a class="btn solid">Sign Up Now</a>
</section>

<footer class="foot">
  <div class="brand"><span class="mark"></span>Velmor Plate Kitchen</div>
  <nav class="links"><a class="on">HOME</a>|<a>MEAL PLANS</a>|<a>PRICING</a>|<a>CONTACT</a>|<a>PRIVACY</a>|<a>TERMS OF USE</a></nav>
  <h3 class="head">Stay in <b>touch</b></h3>
  <div class="contact"><b>TORONTO:</b> 416-555-0188 <b>EMAIL:</b> sales@velmorplatekitchen.com</div>
  <svg class="up" width="20" height="24" viewBox="0 0 20 24"><path d="M10 22V3M3 10l7-7 7 7" fill="none" stroke="#1c9fe0" stroke-width="2.5"/></svg>
</footer>
<div class="bottombar">
  <span>Copyright © 2018 Velmor Plate Kitchen. All Rights Reserved</span>
  <div class="social"><i></i><i></i><i></i><i></i><i></i></div>
</div>

</body>
</html>
```